THE SHRIEKING AT BRAMBLEMOOR Prospectus/Deck

We need a prospectus/deck made for this Halloween event called THE SHRIEKING AT BRAMBLEMOOR. Attached is the writeup, our logo, some background photos you can use, and photos of the actual town site. For the town photos (4) could you try to make them look greyscale or smokey? I attached a sample Prospectus/Deck that was created for another event of ours to give you an idea of layout and pages.

```html
<!DOCTYPE html>
<html lang="en">
<head>
<meta charset="utf-8">
<title>The Shrieking at Bramblemoor – Prospectus</title>
<link href="https://fonts.googleapis.com/css2?family=Poppins:wght@300;400;500;600;700;800&display=swap" rel="stylesheet">
<style>
:root{
  --canvas:#e8e8e8;
  --ink:#000;
  --white:#fff;
  --green:#8cc43f;
  --green-dark:#5f9a2a;
  --gold:#d9b83a;
  --gold-dark:#8a7422;
  --card:#1b1b1b;
  --muted:#d6d6d6;
}
*{margin:0;padding:0;box-sizing:border-box}
html,body{width:1200px;height:2400px;overflow:hidden;background:var(--canvas);font-family:'Poppins',sans-serif;color:var(--white)}
.deck{position:absolute;left:0;top:0;width:1288px;height:2576px;transform:scale(0.93168);transform-origin:0 0}
.page{position:absolute;left:241px;width:810px;height:573px;background:var(--ink);overflow:hidden}
.page--cover{top:83px}
.page--intro{top:693px}
.page--vendors{top:1300px}
.page--tiers{top:1912px}
.abs{position:absolute}
.photo{position:absolute}
.green{color:var(--green)}
.gold{color:var(--gold)}

/* cover */
.cover-photo{left:400px;top:0;width:410px;height:573px;background:radial-gradient(ellipse at 55% 45%,#4a5a22 0%,#2b3414 40%,#15190a 70%,#050604 100%)}
.cover-fade{left:340px;top:0;width:160px;height:573px;background:linear-gradient(90deg,#000,rgba(0,0,0,0))}
.cover-frame{left:458px;top:38px;width:319px;height:495px;border:6px solid #4d4218}
.cover-welcome{left:45px;top:92px;font-size:35px;font-weight:400;letter-spacing:.5px}
.brand-kicker{font-weight:500;color:var(--gold);letter-spacing:5px}
.cover-kicker{left:104px;top:168px;font-size:17px}
.brand-word{font-weight:800;color:var(--green);letter-spacing:-.5px}
.cover-brand{left:46px;top:192px;font-size:48px}
.cover-lede{left:45px;top:322px;width:380px;font-size:21px;line-height:27px;font-weight:400}
.cover-lede b{font-weight:600}
.cover-rule{left:45px;top:430px;width:385px;height:1px;background:#444}
.cover-pill{left:70px;top:426px;width:97px;height:9px;border-radius:5px;background:linear-gradient(90deg,var(--gold),var(--green))}
.url{letter-spacing:1px}
.cover-url{left:45px;top:462px;font-size:18px;letter-spacing:2px}

/* shared footer */
.foot-brand{left:38px;top:500px}
.foot-brand .brand-kicker{display:block;font-size:5.5px;letter-spacing:2px;margin-left:14px}
.foot-brand .brand-word{display:block;font-size:17px;line-height:20px}
.foot-url{right:60px;top:509px;font-size:13px}
.page-badge{right:26px;top:508px;width:22px;height:22px;border-radius:50%;background:var(--gold);color:#000;font-size:8px;font-weight:600;display:flex;align-items:center;justify-content:center}

/* intro */
.intro-label{left:40px;top:255px;transform:rotate(-90deg);transform-origin:0 0;font-size:24px;font-weight:300;color:var(--green);letter-spacing:1px}
.intro-copy{left:91px;top:45px;width:370px;font-size:8.3px;line-height:11.5px;text-align:justify}
.intro-copy p+p{margin-top:12px}
.intro-photo{left:497px;top:47px;width:265px;height:420px;background:linear-gradient(170deg,#9aa39a 0%,#6f7a62 35%,#3c4a2a 70%,#1e2614 100%);clip-path:polygon(0 0,95% 0,100% 4%,100% 100%,0 100%)}
.intro-frame{left:506px;top:57px;width:268px;height:415px;border:1px solid #cfcfcf}
.section-head{font-size:17.5px;font-weight:700;letter-spacing:-.2px}
.about-head{left:43px;top:270px}
.about-copy{left:43px;top:297px;width:418px;font-size:8.3px;line-height:11.5px}
.dates{left:41px;top:383px;width:416px;height:94px;background:linear-gradient(180deg,var(--gold) 0%,#b6c23a 45%,var(--green-dark) 100%);clip-path:polygon(20px 0,100% 0,100% 78%,94% 100%,0 100%,0 20px);color:#111}
.dates-label{position:absolute;left:26px;top:8px;font-size:16px;font-weight:400}
.dates-label b{font-weight:700}
.dates-rule{position:absolute;left:165px;top:20px;width:230px;height:1px;background:rgba(0,0,0,.35)}
.dates-main{position:absolute;left:24px;top:22px;font-size:31px;font-weight:700;letter-spacing:-.5px}
.dates-place{position:absolute;left:26px;top:62px;font-size:14.5px;display:flex;align-items:center;gap:4px}

/* vendors */
.vendors-ground{left:0;top:330px;width:810px;height:243px;background:linear-gradient(180deg,#000 0%,#0d1208 40%,#1a2212 100%)}
.vendor-photo{left:36px;top:44px;width:335px;height:238px;border:2px solid #ddd;background:linear-gradient(135deg,#6f655a 0%,#4c4a46 45%,#2f3140 100%)}
.vendor-head{left:404px;top:42px}
.vendor-copy{left:404px;top:73px;width:372px;font-size:8.6px;line-height:11.5px}
.vendor-copy p+p{margin-top:11px}
.vendor-copy .tag{color:var(--gold);font-weight:600}
.vendor-list{left:404px;top:172px;width:375px;display:grid;grid-template-columns:190px 185px;column-gap:2px;font-size:8.6px;font-weight:600;line-height:11px}
.vendor-list ul{list-style:none}
.vendor-list li{display:flex;gap:6px;margin-bottom:12px}
.tick{flex:0 0 auto;width:9px;height:9px;margin-top:1px}
.truck-banner{left:93px;top:311px;width:624px;height:43px;border-radius:8px;background:linear-gradient(90deg,var(--green) 0%,#c6c53a 50%,var(--gold) 100%);color:#111;font-size:24px;font-weight:700;display:flex;align-items:center;justify-content:center;letter-spacing:.2px}
.promo-copy{left:36px;top:376px;width:470px;font-size:8.6px;line-height:11.5px;text-align:justify}
.promo-copy p+p{margin-top:11px}
.promo-copy .tag{color:var(--gold);font-weight:600}
.street-photo{left:527px;top:372px;width:250px;height:106px;border:2px solid #ddd;background:linear-gradient(160deg,#b9c4cc 0%,#8a8f86 40%,#6e6358 70%,#4c5a3a 100%)}

/* tiers */
.tiers-bg{left:0;top:0;width:810px;height:573px;background:radial-gradient(ellipse at 50% 35%,#1c1c1c 0%,#0b0b0b 60%,#000 100%)}
.tiers-brand{left:0;top:38px;width:810px;text-align:center}
.tiers-brand .brand-kicker{display:block;font-size:7px;letter-spacing:3px}
.tiers-brand .brand-word{display:block;font-size:34px;line-height:40px}
.tiers-head{left:0;top:104px;width:810px;text-align:center;color:var(--green)}
.tiers-intro{left:95px;top:130px;width:620px;text-align:center;font-size:8.6px;line-height:11.5px}
.tier{position:absolute;top:180px;width:222px;height:233px;background:var(--card);border-radius:10px}
.tier--platinum{left:44px}
.tier--gold{left:295px}
.tier--silver{left:544px}
.tier-tab{position:absolute;left:16px;top:-12px;width:190px;height:40px;clip-path:polygon(0 0,100% 0,88% 80%,80% 100%,20% 100%,12% 80%);color:#111;text-align:center;font-size:10px;font-weight:600;line-height:11px;padding-top:9px}
.tier--platinum .tier-tab,.tier--silver .tier-tab{background:linear-gradient(180deg,#8a8a8a,#f2f2f2 55%,#bdbdbd)}
.tier--gold .tier-tab{background:linear-gradient(180deg,#a88a1e,#f3d36a 55%,#c9a632)}
.tier-price{position:absolute;left:0;top:38px;width:100%;text-align:center;font-size:17px;font-weight:700;color:var(--green)}
.tier-perks{position:absolute;left:13px;top:66px;width:190px;list-style:none;font-size:6.8px;line-height:8.4px}
.tier-perks li{display:flex;gap:4px;margin-bottom:10px}
.tier-perks .tick{width:7px;height:7px}
.tier-bar{position:absolute;left:35px;bottom:0;width:155px;height:10px;border-radius:8px 8px 0 0;background:linear-gradient(90deg,var(--green),#b8c23a)}
.tiers-note{top:430px;font-size:8.6px;line-height:11.5px}
.tiers-note p+p{margin-top:11px}
.tiers-note--left{left:44px;width:265px}
.tiers-note--right{left:350px;width:410px}
.tiers-url{left:0;top:508px;width:810px;text-align:center;font-size:14px;letter-spacing:2px}
</style>
</head>
<body>
<svg width="0" height="0" style="position:absolute">
  <symbol id="tick" viewBox="0 0 10 10">
    <circle cx="5" cy="5" r="5" fill="#8cc43f"/>
    <path d="M2.8 5.2 L4.4 6.7 L7.3 3.5" fill="none" stroke="#111" stroke-width="1.3" stroke-linecap="round" stroke-linejoin="round"/>
  </symbol>
</svg>

<main class="deck">

  <!-- Cover -->
  <section class="page page--cover">
    <div class="photo cover-photo" role="img" aria-label="Masked forest creature in a dark green robe standing among autumn leaves"></div>
    <div class="abs cover-fade"></div>
    <div class="abs cover-frame"></div>
    <h1 class="abs cover-welcome">WELCOME TO</h1>
    <div class="abs cover-kicker brand-kicker">THE SHRIEKING AT</div>
    <div class="abs cover-brand brand-word">BRAMBLEMOOR</div>
    <p class="abs cover-lede"><b>The Shrieking at Bramblemoor</b> is a premier haunted town attraction known for its immersive</p>
    <div class="abs cover-rule"></div>
    <div class="abs cover-pill"></div>
    <div class="abs cover-url url">www.<span class="gold">shriekingatbramblemoor</span>.ca</div>
  </section>

  <!-- Introduction -->
  <section class="page page--intro">
    <h2 class="abs intro-label">INTRODUCTION</h2>
    <div class="abs intro-copy">
      <p>Welcome to The Shrieking at Bramblemoor, where terror meets Hollywood magic! Step into our nightmare-inducing event set within a sprawling film studio lot at 1420 Concession Road 9, Ashbury, Ontario L0K 2B0 which has been transformed into a chillingly realistic little town. As you enter, you will find yourself immersed in the eerie atmosphere of a bygone era, where each corner holds lurking horrors. Our haunted experience offers a unique opportunity for vendors to become part of the terror by occupying the shops that line the Main Street of this sinister town. From creepy curiosities to spine-chilling treats, your store front will become a focal point of fear, allowing visitors to not only scream but also shop amidst the horrors. Prepare for a spine-tingling journey like no other as you explore our haunted event in this hauntingly realistic town.</p>
      <p>The Shrieking at Bramblemoor is an an exhilarating and spine-chilling haunted town experience that promises to deliver unforgettable thrills and scares. As we gear up for another terrifying season, we invite you to join us as a valued vendor or sponsor. This prospectus outlines the various opportunities available for your brand to be part of this highly anticipated event.</p>
    </div>
    <div class="photo intro-photo" role="img" aria-label="Pale robed figure with a branch headdress in a misty overgrown field"></div>
    <div class="abs intro-frame"></div>
    <h2 class="abs about-head section-head"><span class="green">ABOUT THE</span> SHRIEKING AT BRAMBLEMOOR</h2>
    <p class="abs about-copy">The Shrieking at Bramblemoor is a premier haunted town attraction known for its immersive and interactive experience that pushes the boundaries of fear. Our haunted town offers a meticulously designed setting with elaborate sets, talented actors, and cutting-edge special effects to create an atmosphere of horror and suspense. We attract a diverse audience of thrill-seekers, horror enthusiasts, families, and groups of friends, ensuring a wide reach for your brand.</p>
    <div class="abs dates">
      <div class="dates-label">EVENT <b>DATES</b></div>
      <div class="dates-rule"></div>
      <div class="dates-main">OCTOBER 6 – 31, 2023</div>
      <div class="dates-place">
        <svg width="11" height="14" viewBox="0 0 12 16"><path d="M6 0C2.7 0 0 2.6 0 5.9 0 10.3 6 16 6 16s6-5.7 6-10.1C12 2.6 9.3 0 6 0zm0 8.3A2.4 2.4 0 1 1 6 3.5a2.4 2.4 0 0 1 0 4.8z" fill="#111"/></svg>
        1420 Concession Road 9, Ashbury, Ontario L0K 2B0
      </div>
    </div>
    <div class="abs foot-brand"><span class="brand-kicker">THE SHRIEKING AT</span><span class="brand-word">BRAMBLEMOOR</span></div>
    <div class="abs foot-url">www.shriekingatbramblemoor.ca</div>
    <div class="abs page-badge">01</div>
  </section>

  <!-- Vendor opportunities -->
  <section class="page page--vendors">
    <div class="photo vendors-ground" role="img" aria-label="Dark cornfield at night"></div>
    <div class="photo vendor-photo" role="img" aria-label="Grimy actor leaning over a workbench in a derelict shop interior"></div>
    <h2 class="abs vendor-head section-head"><span class="green">VENDOR</span> OPPORTUNITIES</h2>
    <div class="abs vendor-copy">
      <p><span class="tag">ON-SITE VENDORS:</span> Starting at $2500 + HST (per vendor; no sharing) depending on location and type of products/services sold and offered.</p>
      <p>Set up your booth within the haunted town premises and showcase your products or services to a captive audience in one of the existing buildings. Your brand will be exposed to thousands of visitors throughout the event. Examples of suitable vendors include:</p>
    </div>
    <div class="abs vendor-list">
      <ul>
        <li><svg class="tick"><use href="#tick"/></svg>Halloween costume shops</li>
        <li><svg class="tick"><use href="#tick"/></svg>Horror-themed merchandise</li>
        <li><svg class="tick"><use href="#tick"/></svg>Local/Artisan food vendors<br>(pre-packaged items)</li>
        <li><svg class="tick"><use href="#tick"/></svg>Face painting and special effects<br>makeup artists</li>
      </ul>
      <ul>
        <li><svg class="tick"><use href="#tick"/></svg>Paranormal investigators or<br>ghost tour guides</li>
        <li><svg class="tick"><use href="#tick"/></svg>Novelty and souvenir vendors</li>
        <li><svg class="tick"><use href="#tick"/></svg>Psychic</li>
        <li><svg class="tick"><use href="#tick"/></svg>Metaphysical items and crystals</li>
      </ul>
    </div>
    <div class="abs truck-banner">FOOD TRUCKS $5000 + HST max of 3-4 total</div>
    <div class="abs promo-copy">
      <p><span class="tag">Promotional Giveaways:</span> Partner with us to provide branded merchandise or samples to be distributed to our visitors. This opportunity allows you to directly engage with attendees and create lasting impressions of your brand.</p>
      <p><span class="tag">Exclusive Sponsorship:</span> Become an exclusive sponsor of The Shrieking at Bramblemoor. This comprehensive package offers maximum exposure and recognition for your brand. Benefits may include prominent logo placement, branding on event merchandise, on-site signage, social media promotions, and more. This option is ideal for businesses looking to establish a strong association with the haunted town and its audience.</p>
    </div>
    <div class="photo street-photo" role="img" aria-label="Aerial view of the town set main street"></div>
    <div class="abs foot-brand"><span class="brand-kicker">THE SHRIEKING AT</span><span class="brand-word">BRAMBLEMOOR</span></div>
    <div class="abs foot-url">www.shriekingatbramblemoor.ca</div>
    <div class="abs page-badge">02</div>
  </section>

  <!-- Sponsorship tiers -->
  <section class="page page--tiers">
    <div class="photo tiers-bg" role="img" aria-label="Dark misty treeline"></div>
    <div class="abs tiers-brand"><span class="brand-kicker">THE SHRIEKING AT</span><span class="brand-word">BRAMBLEMOOR</span></div>
    <h2 class="abs tiers-head section-head">SPONSORSHIP TIERS</h2>
    <p class="abs tiers-intro">We offer different sponsorship tiers to suit your marketing goals and budget. Please note that availability is limited for each tier, and commitments will be honored on a first-come, first-served basis. The sponsorship tiers include:</p>

    <article class="tier tier--platinum">
      <div class="tier-tab">PLATINUM<br>SPONSORSHIP</div>
      <div class="tier-price">$15,000 + HST</div>
      <ul class="tier-perks">
        <li><svg class="tick"><use href="#tick"/></svg>Prominent logo placement on all marketing materials, including website, posters, flyers, and social media promotions</li>
        <li><svg class="tick"><use href="#tick"/></svg>Exclusive branding on event merchandise</li>
        <li><svg class="tick"><use href="#tick"/></svg>On-site signage and banners featuring your brand</li>
        <li><svg class="tick"><use href="#tick"/></svg>Dedicated social media posts highlighting your sponsorship</li>
        <li><svg class="tick"><use href="#tick"/></svg>Recognition during event announcements and media interviews</li>
        <li><svg class="tick"><use href="#tick"/></svg>Complimentary tickets for your staff or clients</li>
      </ul>
      <div class="tier-bar"></div>
    </article>

    <article class="tier tier--gold">
      <div class="tier-tab">GOLD<br>SPONSORSHIP</div>
      <div class="tier-price">$10,000 + HST</div>
      <ul class="tier-perks">
        <li><svg class="tick"><use href="#tick"/></svg>Logo placement on select marketing materials, including website, posters, and social media promotions</li>
        <li><svg class="tick"><use href="#tick"/></svg>On-site signage featuring your brand</li>
        <li><svg class="tick"><use href="#tick"/></svg>Social media mentions acknowledging your sponsorship</li>
        <li><svg class="tick"><use href="#tick"/></svg>Complimentary tickets for your staff or clients</li>
      </ul>
      <div class="tier-bar"></div>
    </article>

    <article class="tier tier--silver">
      <div class="tier-tab">SILVER<br>SPONSORSHIP</div>
      <div class="tier-price">$5,000 + HST</div>
      <ul class="tier-perks">
        <li><svg class="tick"><use href="#tick"/></svg>Logo placement on event website and select marketing materials</li>
        <li><svg class="tick"><use href="#tick"/></svg>On-site signage featuring your brand</li>
        <li><svg class="tick"><use href="#tick"/></svg>Complimentary tickets for your staff or clients</li>
      </ul>
      <div class="tier-bar"></div>
    </article>

    <div class="abs tiers-note tiers-note--left">
      <p>We are open to customizing sponsorship packages to meet your specific needs and objectives.</p>
      <p>If you are interested in becoming a vendor or sponsor for The Shrieking at Bramblemoor, please contact us at the following: <b>mara@nightfallevents.ca</b></p>
    </div>
    <div class="abs tiers-note tiers-note--right">
      <p>We would be delighted to discuss the available opportunities in more detail and tailor a package that aligns with your brand's goals.</p>
      <p>Do not miss the chance to be part of a frightfully fantastic experience that will haunt your customers' memories for years to come. Join The Shrieking at Bramblemoor as a vendor or sponsor and make this haunted town season one to remember!</p>
    </div>
    <div class="abs tiers-url url">www.<span class="green">shriekingatbramblemoor</span>.ca</div>
  </section>

</main>
</body>
</html>
```